The Pipe Lantern business cards

Hi
i have attached a photo, this is how i want the front of my business card to look like:
i want the water drop on the right to be orange
and the water drop on the left to be gloss black
"The" and "Pty Ltd." will be in the same orange as the water drop
and "Pipe Lantern" will be in white
The background of the logo will be a matte black
on the back of the business card i need the following info:
'The Pipe Lantern pty ltd. '
'Plumbing . Drainage . Gas Fitting . Roofing . Jet Blasting . CCTV . '
Also my contact details:
Cal Yardley
0418672913
thepipelantern@mailkestrel.com
Licence# 583016K
Target Market(s)
Strata managers, building managers, the general public
Industry/Entity Type
Business

```html
<!DOCTYPE html>
<html lang="en">
<head>
<meta charset="utf-8">
<title>The Pipe Lantern – Business Cards</title>
<link href="https://fonts.googleapis.com/css2?family=Source+Sans+3:ital,wght@0,400;0,600;1,400;1,600&display=swap" rel="stylesheet">
<style>
  :root {
    --page: #ffffff;
    --card: #111414;
    --orange: #f7800f;
    --white: #ffffff;
    --shadow: rgba(0, 0, 0, 0.55);
  }
  * { margin: 0; padding: 0; box-sizing: border-box; }
  html, body {
    width: 1200px;
    height: 1000px;
    overflow: hidden;
    background: var(--page);
    font-family: "Source Sans 3", "Myriad Pro", sans-serif;
  }
  .card {
    position: absolute;
    width: 724px;
    height: 433px;
    background: var(--card);
    box-shadow: 4px 6px 8px var(--shadow);
  }
  .card--front { left: 238px; top: 32px; }
  .card--back  { left: 238px; top: 534px; width: 722px; }

  .brand-mark {
    position: absolute;
    left: 122px;
    top: 100px;
  }
  .brand-article,
  .brand-name,
  .brand-suffix {
    position: absolute;
    text-align: right;
    font-weight: 600;
    white-space: nowrap;
  }
  .brand-article {
    right: 177px;
    top: 104px;
    color: var(--orange);
    font-size: 44px;
    line-height: 44px;
  }
  .brand-name {
    right: 62px;
    top: 152px;
    color: var(--white);
    font-size: 66px;
    line-height: 66px;
  }
  .brand-suffix {
    right: 96px;
    top: 298px;
    color: var(--orange);
    font-size: 26px;
    line-height: 28px;
  }

  .details {
    position: absolute;
    left: 53px;
    top: 89px;
    color: var(--white);
    font-style: italic;
    font-size: 22px;
    line-height: 28.5px;
  }
  .details__company {
    color: var(--orange);
    font-size: 38px;
    line-height: 44px;
    margin-bottom: 4px;
  }
  .details__services { margin-bottom: 29px; }
  .contact-line {
    display: flex;
    align-items: center;
    gap: 12px;
  }
  .contact-line svg { width: 27px; height: 22px; flex: none; }
  .social-square {
    position: absolute;
    left: 53px;
    top: 367px;
    width: 39px;
    height: 39px;
    border: 3px solid var(--white);
    border-radius: 6px;
  }
</style>
</head>
<body>
  <section class="card card--front">
    <svg class="brand-mark" width="180" height="180" viewBox="0 0 180 180" aria-hidden="true">
      <circle cx="90" cy="90" r="84" fill="none" stroke="var(--orange)" stroke-width="8"/>
    </svg>
    <div class="brand-article">THE</div>
    <div class="brand-name">Pipe<br>Lantern</div>
    <div class="brand-suffix">Pty Ltd.</div>
  </section>

  <section class="card card--back">
    <div class="details">
      <p class="details__company">The Pipe Lantern Pty Ltd.</p>
      <p class="details__services">Plumbing . Drainage . Gas Fitting . Roofing . Jet Blasting . CCTV .<br>Domestic . Commercial . Industrial . Maintenance</p>
      <p class="details__person">Cal Yardley</p>
      <p class="contact-line">
        <svg viewBox="0 0 27 22" aria-hidden="true">
          <path d="M5 2 L9 1.5 L11.5 7 L9 9 C10.5 12 12.5 14 15.5 15.5 L17.5 13 L23 15.5 L22.5 19.5 C21 21 18 21 14 19 C9 16.5 5.5 12.5 3.5 8 C2 5 3 3 5 2 Z" fill="var(--white)"/>
        </svg>
        <span>0418 672 913</span>
      </p>
      <p class="contact-line">
        <svg viewBox="0 0 27 22" aria-hidden="true">
          <rect x="1" y="4" width="25" height="15" fill="var(--white)"/>
          <path d="M1 4 L13.5 13 L26 4" fill="none" stroke="var(--card)" stroke-width="1.6"/>
        </svg>
        <span>thepipelantern@mailkestrel.com</span>
      </p>
      <p class="details__licence">Licence# 583016K</p>
    </div>
    <div class="social-square" aria-hidden="true"></div>
  </section>
</body>
</html>
```